Ridgeway Insulcoat Works Spray Foam Appications website

We need a custom website for our company, www.ridgewayinsulcoatworks.example. We need something we can modify by adding/changing content, photos, updated projects, etc. We are a commercial contractor specializing in Spray Foam applications. We want the website to be very creative and easy to navigate. The main points of the website are to showcase our projects, and describe our scope of services. We provide spray foam applications to the residential and commercial market. We offer Spray Foam roofing applications, as well as Spray Foam interior insulation applications. We also provide Roof Restoration Coating Systems to refurbish old and failing metal roofs. We would be ok with a one page web design if we can get the scope of our services to flow in a single page. The designer can decide if single or multiple pages works best for our business. One of the suppliers we work with is www.vantrexo.example.

Target Market(s)

Residential Home Builders, General Contractors, Commercial Construction Companies, Property Management Groups.

Industry/Entity Type

Insulation

Number of Pages Required

5+ page

Font styles to use
Serif
Sans Serif

Colors

Designer to choose colors to be used in the design.

Requirements
Must have
• We already have a Wix page, so website must be a Wix theme design. Nice easy to navigate format. Color matched to our current logo theme. We already have brochures and would like for it to match what's already in the hands of some of our customers. Need to be able to manage content to update photos, projects, scope of service, etc., via Wix. Current hold/splash page is hosted at www.ridgewayinsulcoatworks.example. We would also like to have this video posted on the home page: https://www.videohost.example/watch?v=QzT4kLp9wXe&feature=share
Nice to have
• I have attached some splash videos, being able to incorporate these somehow without being overpowering would be nice.

```html
<!DOCTYPE html>
<html lang="en">
<head>
<meta charset="utf-8">
<title>Ridgeway Insulcoat Works — Spray Foam Applications</title>
<link href="https://fonts.googleapis.com/css2?family=Montserrat:wght@400;500;600;700&family=Raleway:ital,wght@0,300;0,400;0,500;1,400;1,500&family=Great+Vibes&display=swap" rel="stylesheet">
<style>
:root{
  --accent:#f5b21d;
  --accent-dark:#e0a010;
  --ink:#262626;
  --text:#4a4a4a;
  --muted:#a6a6a6;
  --line:#e6e6e6;
  --dark:#2f2f2f;
  --darker:#262626;
  --white:#ffffff;
}
*{margin:0;padding:0;box-sizing:border-box}
html,body{width:1200px;height:3694px;overflow:hidden}
body{background:var(--white);font-family:"Raleway",sans-serif;color:var(--text);position:relative}
.section{position:absolute;left:0;width:1200px}
.abs{position:absolute}
.btn{position:absolute;background:var(--accent);color:var(--white);font-family:"Montserrat",sans-serif;font-weight:600;font-size:11px;letter-spacing:.3px;display:flex;align-items:center;justify-content:center;text-transform:uppercase;border-radius:2px}
.heading{position:absolute;font-family:"Montserrat",sans-serif;font-weight:600;font-size:30px;color:var(--ink);letter-spacing:-.5px;line-height:1}
.heading .dot{color:var(--accent)}
.rule{position:absolute;height:2px;background:var(--accent)}
.rule.double::after{content:"";position:absolute;left:8px;right:8px;top:5px;height:2px;background:var(--accent)}
.rule.double{height:2px}

/* header */
.site-header{top:0;height:93px;background:var(--white)}
.brand{left:161px;top:25px;display:flex;align-items:center;gap:8px}
.brand-mark{width:44px;height:44px;border:3px solid var(--accent);border-radius:50%}
.brand-name{font-family:"Montserrat",sans-serif;font-weight:600;font-size:12px;color:var(--accent);width:120px;line-height:1.25}
.nav a{position:absolute;top:40px;font-family:"Montserrat",sans-serif;font-size:12px;color:var(--ink);text-decoration:none;letter-spacing:.3px}
.nav a.current{color:var(--accent);border-bottom:1px solid var(--accent);padding-bottom:2px}
.caret{display:inline-block;width:0;height:0;border-left:3px solid transparent;border-right:3px solid transparent;border-top:4px solid var(--ink);margin-left:4px;vertical-align:middle}

/* hero */
.hero{top:93px;height:601px;background:linear-gradient(180deg,#5a5a5a 0%,#4b4b4b 30%,#3b3b3b 70%,#3d3d3d 100%)}
.hero-band{left:0;top:188px;width:1200px;height:204px;background:rgba(38,38,38,.88)}
.hero-title{top:183px;left:0;width:1200px;text-align:center;font-family:"Montserrat",sans-serif;font-weight:600;font-size:46px;letter-spacing:4px;color:var(--white);line-height:44px}
.hero-title em{color:var(--accent);font-style:italic}
.hero-sub{top:292px;left:0;width:1200px;text-align:center;font-family:"Raleway",sans-serif;font-size:24px;color:var(--white);letter-spacing:.5px}
.slide-arrow{position:absolute;width:45px;height:45px;display:flex;align-items:center;justify-content:center}
.slide-arrow.prev{left:162px;top:278px;background:var(--accent)}
.slide-arrow.next{left:991px;top:278px;border:2px solid var(--accent)}

/* who we are */
.about{top:694px;height:515px;border-bottom:1px solid var(--line)}
.about-media{left:162px;top:138px;width:401px;height:315px;background:linear-gradient(180deg,#7d8fa1 0%,#9aa6ae 35%,#b4a878 60%,#8f8468 100%)}
.play{position:absolute;left:154px;top:110px;width:95px;height:95px;border-radius:50%;border:6px solid var(--accent);background:var(--white);display:flex;align-items:center;justify-content:center}
.about-copy{left:609px;top:50px;width:430px;font-size:11.5px;line-height:22.5px;color:#b3b3b3;font-weight:300}
.checklist{left:650px;top:211px;list-style:none}
.checklist li{height:30px;display:flex;align-items:center;gap:9px;font-size:12px;color:var(--ink)}
.checklist svg{flex:none}
.sign-name{left:886px;top:1102px;font-family:"Montserrat",sans-serif;font-size:11px;font-weight:600;color:var(--ink)}
.sign-script{left:884px;top:1116px;font-family:"Great Vibes",cursive;font-size:30px;color:#b8b8b8}

/* services */
.services{top:1209px;height:593px}
.services-copy{left:161px;top:130px;width:430px;font-size:11.5px;line-height:22.5px;color:var(--text)}
.services-copy p+p{margin-top:12px}
.service-card{position:absolute;width:202px}
.service-card .thumb{width:202px;height:149px}
.service-card h3{margin-top:12px;font-family:"Raleway",sans-serif;font-weight:400;font-size:15px;color:var(--ink)}
.service-card p{margin-top:6px;font-size:11px;line-height:23px;color:var(--muted);font-weight:300}

/* work */
.work{top:1802px;height:744px;background:var(--dark)}
.work .heading{color:var(--white)}
.tabs{left:311px;top:151px;width:578px;height:44px;background:#4a4a4a;display:flex}
.tabs span{flex:1;display:flex;align-items:center;justify-content:center;font-family:"Montserrat",sans-serif;font-size:11.5px;color:var(--white)}
.tabs span.active{color:var(--accent);border-top:2px solid var(--accent);background:#3f3f3f}
.tile{position:absolute;width:202px;height:202px}
.tile.featured{background:var(--accent);padding:52px 22px 0}
.tile.featured h4{font-family:"Montserrat",sans-serif;font-size:15px;font-weight:600;color:var(--white)}
.tile.featured p{margin-top:6px;font-size:10.5px;line-height:22px;color:#fff3d3;font-weight:300}

/* cta */
.cta{top:2546px;height:270px;background:linear-gradient(180deg,#4a4a48 0%,#3e3f3c 50%,#333431 100%)}
.cta-frame{left:162px;top:59px;width:877px;height:149px;border:6px solid rgba(255,255,255,.18)}
.cta-text{left:0;top:88px;width:1200px;text-align:center;font-family:"Raleway",sans-serif;font-weight:700;font-size:23px;color:var(--white)}

/* why */
.why{top:2816px;height:473px}
.why-card{position:absolute;width:277px;height:119px;border:1px solid var(--line)}
.why-card.highlight{border:2px solid var(--accent)}
.why-icon{position:absolute;left:5px;top:35px;width:43px;height:43px;background:#f3f3f3;display:flex;align-items:center;justify-content:center}
.highlight .why-icon{background:var(--accent)}
.why-card h3{position:absolute;left:58px;top:20px;font-family:"Raleway",sans-serif;font-weight:400;font-size:15px;color:var(--ink)}
.why-card p{position:absolute;left:59px;top:50px;width:205px;font-size:10px;line-height:17px;color:var(--muted);font-weight:300}

/* testimonials */
.testimonials{top:3289px;height:350px;background:var(--accent)}
.testimonials .heading{color:var(--white)}
.testimonials .rule,.testimonials .rule.double::after{background:var(--white)}
.quote{left:230px;top:162px;width:740px;text-align:center;font-style:italic;font-weight:500;font-size:12.5px;line-height:23px;color:var(--ink)}
.author{left:0;top:252px;width:1200px;text-align:center;font-style:italic;font-size:12px;color:var(--white)}
.author b{font-weight:700}
.stars{left:0;top:274px;width:1200px;text-align:center;color:var(--white);font-size:13px;letter-spacing:3px}
.circle-arrow{position:absolute;width:30px;height:30px;border-radius:50%;display:flex;align-items:center;justify-content:center}
.circle-arrow.prev{left:163px;top:183px;border:2px solid var(--white)}
.circle-arrow.next{left:1009px;top:183px;background:var(--white)}
</style>
</head>
<body>

<header class="section site-header">
  <div class="abs brand">
    <span class="brand-mark"></span>
    <span class="brand-name">Ridgeway Insulcoat Works</span>
  </div>
  <nav class="nav">
    <a class="current" href="#" style="left:384px">HOME</a>
    <a href="#" style="left:459px">ABOUT</a>
    <a href="#" style="left:539px">PRODUCTS<span class="caret"></span></a>
    <a href="#" style="left:645px">SERVICES<span class="caret"></span></a>
    <a href="#" style="left:742px">OUR TEAM</a>
    <a href="#" style="left:846px">TESTIMONIALS</a>
    <a href="#" style="left:975px">CONTACT</a>
  </nav>
</header>

<section class="section hero" role="img" aria-label="Crew of workers standing on a metal warehouse roof">
  <div class="abs hero-band"></div>
  <h1 class="abs hero-title">LOREM IPSUM <em>DOLOR AMET</em><br>NINGUN POSTEKAM</h1>
  <p class="abs hero-sub">With Flexibility And Unique Technology</p>
  <a class="slide-arrow prev" href="#"><svg width="12" height="12" viewBox="0 0 12 12"><path d="M8 1 3 6l5 5" fill="none" stroke="#fff" stroke-width="2"/></svg></a>
  <a class="slide-arrow next" href="#"><svg width="12" height="12" viewBox="0 0 12 12"><path d="M4 1l5 5-5 5" fill="none" stroke="#fff" stroke-width="2"/></svg></a>
  <a class="btn" href="#" style="left:532px;top:366px;width:136px;height:44px">Learn More</a>
</section>

<section class="section about">
  <h2 class="heading" style="left:162px;top:57px">WHO WE ARE<span class="dot">.</span></h2>
  <div class="rule double" style="left:162px;top:95px;width:60px"></div>
  <div class="abs about-media" role="img" aria-label="Video thumbnail of a foam-coated warehouse roof">
    <div class="play"><svg width="28" height="30" viewBox="0 0 28 30"><path d="M2 1l25 14L2 29z" fill="#f5b21d"/></svg></div>
  </div>
  <p class="abs about-copy">Swag kogi knausgaard typewriter, portland freegan intelligentsia man braid. Fanny pack street art fixie listicle tofu bespoke hoodie dreamcatcher put a bird on it. Typewriter tousled street art whatever messenger bag williamsburg vegan occupy chambray man bun four loko tbh. Intelligentsia brooklyn pour-over pickled literally. Street art kinfolk live-edge chicharrones poutine. Slow-carb artisan meditation actually. Shaman echo park semiotics vinyl kale</p>
  <ul class="abs checklist">
    <li><svg width="16" height="16" viewBox="0 0 16 16"><circle cx="8" cy="8" r="7" fill="none" stroke="#f5b21d" stroke-width="1.4"/><path d="M7 5l3 3-3 3" fill="none" stroke="#f5b21d" stroke-width="1.4"/></svg>Voluptatem acusantium doloremque laudantium totam</li>
    <li><svg width="16" height="16" viewBox="0 0 16 16"><circle cx="8" cy="8" r="7" fill="none" stroke="#f5b21d" stroke-width="1.4"/><path d="M7 5l3 3-3 3" fill="none" stroke="#f5b21d" stroke-width="1.4"/></svg>Nemo enim ipsam voluptatem quia voluptas sit</li>
    <li><svg width="16" height="16" viewBox="0 0 16 16"><circle cx="8" cy="8" r="7" fill="none" stroke="#f5b21d" stroke-width="1.4"/><path d="M7 5l3 3-3 3" fill="none" stroke="#f5b21d" stroke-width="1.4"/></svg>Quasi architecto beatae vitae dicta sunt explicabo</li>
    <li><svg width="16" height="16" viewBox="0 0 16 16"><circle cx="8" cy="8" r="7" fill="none" stroke="#f5b21d" stroke-width="1.4"/><path d="M7 5l3 3-3 3" fill="none" stroke="#f5b21d" stroke-width="1.4"/></svg>Voluptatem acusantium doloremque laudantium totam</li>
    <li><svg width="16" height="16" viewBox="0 0 16 16"><circle cx="8" cy="8" r="7" fill="none" stroke="#f5b21d" stroke-width="1.4"/><path d="M7 5l3 3-3 3" fill="none" stroke="#f5b21d" stroke-width="1.4"/></svg>Nemo enim ipsam voluptatem quia voluptas sit</li>
    <li><svg width="16" height="16" viewBox="0 0 16 16"><circle cx="8" cy="8" r="7" fill="none" stroke="#f5b21d" stroke-width="1.4"/><path d="M7 5l3 3-3 3" fill="none" stroke="#f5b21d" stroke-width="1.4"/></svg>Quasi architecto beatae vitae dicta sunt explicabo</li>
  </ul>
  <a class="btn" href="#" style="left:609px;top:408px;width:138px;height:45px">More About Us</a>
  <span class="abs sign-name" style="top:408px">Elena Varga</span>
  <span class="abs sign-script" style="top:418px">Elena Varga</span>
</section>

<section class="section services">
  <h2 class="heading" style="left:162px;top:57px">SERVICES WE DO<span class="dot">.</span></h2>
  <div class="rule double" style="left:162px;top:95px;width:60px"></div>
  <div class="abs services-copy">
    <p>Lorem ipsum dolor sit amet, consectetur adipisicing elit sed do eiusmod tempor incididunt ut labore et dolore magna aliqua. Ut enim ad minim veniam, quis nos-trud exercitation ullamco laboris nisi ut aliquip ex ea com-modo consequat. Duis aute irure dolor in reprehenderit in voluptate velit</p>
    <p>Lomo unicorn kogi mumblecore VHS, seitan chartreuse tumeric shabby chic kale chips narwhal polaroid schlitz jean shorts butcher. Subway tile post-iron-ic fam semiotics meggings hella godard VHS palo santo truffaut succulents lomo. Lyft lumbersexual post-ironic scenester four loko master cleanse. Af bushwick lo-fi palo santo, selfies helvetica cred plaid. Photo booth raw denim letterpress 90's. La croix pour-over pickled letterpress forage helvetica bespoke gentrify kickstarter roof party. Skateboard tumblr XOXO post-ironic jean shorts brunch la croix cardigan mustache pop-up if any lorem ipsum dolor amet ningun postekam vlar dohaeris posteamis drinking brooklyn swag yolo</p>
  </div>
  <a class="btn" href="#" style="left:161px;top:487px;width:137px;height:45px">Go To Services</a>

  <article class="service-card" style="left:612px;top:61px">
    <div class="thumb" role="img" aria-label="Yellow foam-coated metal roof close-up" style="background:linear-gradient(180deg,#d9a92f,#e8bd4a)"></div>
    <h3>Lorem Ipsum Dolor</h3>
    <p>Lorem ipsum dolor amet ningun if a postekam valar mostedar</p>
  </article>
  <article class="service-card" style="left:837px;top:61px">
    <div class="thumb" role="img" aria-label="Roof coating in progress with a traffic cone" style="background:linear-gradient(180deg,#6f93c4 0%,#9fb3c8 30%,#c9c6bd 55%,#a8a397 100%)"></div>
    <h3>Lorem Ipsum Dolor</h3>
    <p>Lorem ipsum dolor amet ningun if a postekam valar mostedar</p>
  </article>
  <article class="service-card" style="left:612px;top:308px">
    <div class="thumb" role="img" aria-label="Insulated interior wall with spray hose" style="background:linear-gradient(180deg,#8f8c84,#d8d5cd 60%,#b9b6ae)"></div>
    <h3>Lorem Ipsum Dolor</h3>
    <p>Lorem ipsum dolor amet ningun if a postekam valar mostedar</p>
  </article>
  <article class="service-card" style="left:837px;top:308px">
    <div class="thumb" role="img" aria-label="Warehouse with newly foamed roof" style="background:linear-gradient(180deg,#4e77b5 0%,#92a6b4 40%,#d4c27d 70%,#c8b66d 100%)"></div>
    <h3>Lorem Ipsum Dolor</h3>
    <p>Lorem ipsum dolor amet ningun if a postekam valar mostedar</p>
  </article>
</section>

<section class="section work">
  <h2 class="heading" style="left:0;width:1200px;text-align:center;top:56px">OUR RECENT WORK/PROJECTS<span class="dot">.</span></h2>
  <div class="rule double" style="left:530px;top:100px;width:60px"></div>
  <div class="abs tabs"><span class="active">ALL</span><span>INDUSTRY</span><span>ROOFING</span><span>LOREM</span><span>IPSUM</span></div>

  <div class="tile" style="left:162px;top:255px;background:linear-gradient(180deg,#5d8fd0,#a9c3df 60%,#8d7a62)" role="img" aria-label="Worker on rebar scaffolding"></div>
  <div class="tile featured" style="left:387px;top:255px">
    <h4>Lorem Ipsum Dolor</h4>
    <p>Lomo unicorn kogi mumblecore VHS, seitan chartreuse tumeric shabby chic kale</p>
  </div>
  <div class="tile" style="left:612px;top:255px;background:linear-gradient(180deg,#9aa3ab,#7c7f80 45%,#d6d8d8)" role="img" aria-label="Industrial plant with coated roof"></div>
  <div class="tile" style="left:837px;top:255px;background:linear-gradient(180deg,#5a7fbd,#b3b8b0 40%,#d8c68a)" role="img" aria-label="Roof coating with traffic cone"></div>
  <div class="tile" style="left:162px;top:480px;background:linear-gradient(160deg,#6a6d70,#c06a2c 50%,#5c5f60)" role="img" aria-label="Worker installing roofing"></div>
  <div class="tile" style="left:387px;top:480px;background:linear-gradient(160deg,#a7c24c,#e6e2dc 45%,#f2f0ec)" role="img" aria-label="Contractor reviewing plans on clipboard"></div>
  <div class="tile" style="left:612px;top:480px;background:linear-gradient(180deg,#8aa0b3,#5f6e5a 30%,#dfe2e3)" role="img" aria-label="White coated metal roof"></div>
  <div class="tile" style="left:837px;top:480px;background:linear-gradient(180deg,#b7c1ca,#dde1e3 55%,#9fa3a5)" role="img" aria-label="Finished roof surface under overcast sky"></div>
</section>

<section class="section cta" role="img" aria-label="Work crew in safety vests on site">
  <div class="abs cta-frame"></div>
  <p class="abs cta-text">Swag kogi knausgaard typewriter, portland freegan intelligentsia man braid</p>
  <a class="btn" href="#" style="left:532px;top:134px;width:136px;height:44px">Request Quote</a>
</section>

<section class="section why">
  <h2 class="heading" style="left:162px;top:55px">WHY CHOOSING US<span class="dot">.</span></h2>
  <div class="rule double" style="left:162px;top:93px;width:60px"></div>

  <div class="why-card" style="left:162px;top:150px"><div class="why-icon"><svg width="22" height="22" viewBox="0 0 22 22" fill="none" stroke="#f5b21d" stroke-width="1.4"><circle cx="11" cy="8" r="4"/><path d="M3 20c1-5 4-7 8-7s7 2 8 7"/></svg></div><h3>30+Years Of Experience</h3><p>Lorem ipsum dolor amet ningun if a onrsti postekam valar mostedar if any one want to buy it</p></div>
  <div class="why-card highlight" style="left:463px;top:150px"><div class="why-icon"><svg width="22" height="22" viewBox="0 0 22 22" fill="none" stroke="#fff" stroke-width="1.4"><circle cx="11" cy="11" r="4"/><path d="M11 2v4M11 16v4M2 11h4M16 11h4M5 5l3 3M14 14l3 3M17 5l-3 3M8 14l-3 3"/></svg></div><h3>Professional Workers</h3><p>Lorem ipsum dolor amet ningun if a onrsti postekam valar mostedar if any one want to buy it</p></div>
  <div class="why-card" style="left:763px;top:150px"><div class="why-icon"><svg width="22" height="22" viewBox="0 0 22 22" fill="none" stroke="#f5b21d" stroke-width="1.4"><path d="M3 3l16 16M19 3 3 19"/><circle cx="4" cy="4" r="2"/><circle cx="18" cy="4" r="2"/></svg></div><h3>Lorem Ipsum Dolor</h3><p>Lorem ipsum dolor amet ningun if a onrsti postekam valar mostedar if any one want to buy it</p></div>
  <div class="why-card" style="left:162px;top:292px"><div class="why-icon"><svg width="22" height="22" viewBox="0 0 22 22" fill="none" stroke="#f5b21d" stroke-width="1.4"><rect x="2" y="4" width="18" height="15"/><path d="M5 15l4-4 3 3 5-6"/></svg></div><h3>800+Succesful Projects</h3><p>Lorem ipsum dolor amet ningun if a onrsti postekam valar mostedar if any one want to buy it</p></div>
  <div class="why-card" style="left:463px;top:292px"><div class="why-icon"><svg width="22" height="22" viewBox="0 0 22 22" fill="none" stroke="#f5b21d" stroke-width="1.4"><circle cx="11" cy="9" r="6"/><path d="M8 17h6M9 20h4M11 6v6"/></svg></div><h3>Reasonable Prices</h3><p>Lorem ipsum dolor amet ningun if a onrsti postekam valar mostedar if any one want to buy it</p></div>
  <div class="why-card" style="left:763px;top:292px"><div class="why-icon"><svg width="22" height="22" viewBox="0 0 22 22" fill="none" stroke="#f5b21d" stroke-width="1.4"><path d="M4 3v6l7 4 7-4V3M11 13v7"/></svg></div><h3>Lorem Ipsum Dolor</h3><p>Lorem ipsum dolor amet ningun if a onrsti postekam valar mostedar if any one want to buy it</p></div>
</section>

<section class="section testimonials">
  <h2 class="heading" style="left:0;width:1200px;text-align:center;top:58px">TESTIMONIALS FEEDBACK<span style="color:#fff">.</span></h2>
  <div class="rule double" style="left:570px;top:98px;width:60px"></div>
  <a class="circle-arrow prev" href="#"><svg width="10" height="10" viewBox="0 0 10 10"><path d="M6.5 1.5 3 5l3.5 3.5" fill="none" stroke="#fff" stroke-width="1.6"/></svg></a>
  <p class="abs quote">Swag kogi knausgaard typewriter, portland freegan intelligentsia man braid. Fanny pack street art fixie listicle tofu bespoke hoodie dreamcatcher put a bird on it. Typewriter tousled street art whatever messenger bag williamsburg vegan occupy chambray man bun four loko tbh</p>
  <a class="circle-arrow next" href="#"><svg width="10" height="10" viewBox="0 0 10 10"><path d="M3.5 1.5 7 5 3.5 8.5" fill="none" stroke="#f5b21d" stroke-width="1.6"/></svg></a>
  <p class="abs author"><b>-ELENA VARGA</b>, Sales Department</p>
  <p class="abs stars">★★★★★</p>
</section>

</body>
</html>
```